Most captivating card ever!

Life Coach - Professional Adventurer - Entrepreneur
I need the worlds most amazing business card for my personal brand. This business card will mostly be used to give to prospective clients for life coaching and business coaching.
Be creative, be adventurous. It needs to stand out. Make people say.. I need this guy!
My background is as an entrepreneur and professional adventurer undertaking extreme expeditions. I am now moving into life coaching.
No specific design ideas, so you have full creativity. Show me your best.
Industry/Entity Type
Life Coaching
Contact Information for Business Card
Dan Pellow
itsdanp.com.au
0468215903
Colors
Designer to choose colors to be used in the design.
Look and feel

```html
<!DOCTYPE html>
<html lang="en">
<head>
<meta charset="utf-8">
<title>Dan Pellow – Business Card</title>
<link href="https://fonts.googleapis.com/css2?family=Oswald:wght@400;500&family=Cutive+Mono&display=swap" rel="stylesheet">
<style>
  :root {
    --paper: #ffffff;
    --backdrop: #eceef3;
    --navy: #262a6b;
    --blue: #1f74b9;
    --sky: #6cb6e4;
    --gold: #f2bd2a;
    --gold-light: #fbe39a;
    --ink-line: #3f4fa8;
    --text-light: #ffffff;
    --strip-line: #cfd1dc;
    --texture: #e6e7ee;
  }
  * { margin: 0; padding: 0; box-sizing: border-box; }
  html, body {
    width: 1200px;
    height: 840px;
    overflow: hidden;
    background: var(--backdrop);
  }
  .card {
    position: relative;
    width: 1200px;
    height: 840px;
    background: var(--paper);
    overflow: hidden;
  }
  .card__art {
    position: absolute;
    inset: 0;
    width: 1200px;
    height: 840px;
  }
  .titles {
    position: absolute;
    left: 70px;
    top: 590px;
    display: flex;
    align-items: center;
    gap: 22px;
    font-family: "Oswald", "Arial Narrow", sans-serif;
    font-weight: 400;
    font-size: 44px;
    letter-spacing: 4px;
    color: var(--text-light);
    white-space: nowrap;
  }
  .titles__dot {
    width: 14px;
    height: 14px;
    border-radius: 50%;
    background: radial-gradient(circle at 35% 35%, var(--gold-light), var(--gold));
  }
  .contact {
    position: absolute;
    left: 0;
    right: 0;
    top: 722px;
    display: flex;
    align-items: baseline;
    padding: 0 70px;
    font-family: "Cutive Mono", "Courier New", monospace;
    font-size: 34px;
    letter-spacing: 5px;
    color: var(--navy);
    white-space: nowrap;
  }
  .contact__name { flex: 0 0 auto; }
  .contact__web { margin-left: 110px; }
  .contact__phone { margin-left: auto; }
</style>
</head>
<body>
  <main class="card">
    <svg class="card__art" viewBox="0 0 1200 840">
      <defs>
        <linearGradient id="tanglewash" x1="0" y1="0" x2="1" y2="1">
          <stop offset="0" stop-color="#eef0fa"/>
          <stop offset="1" stop-color="#dfe3f4"/>
        </linearGradient>
        <linearGradient id="barswash" x1="0" y1="0" x2="1" y2="0">
          <stop offset="0" stop-color="#e7eaf7"/>
          <stop offset="1" stop-color="#f1f2fa"/>
        </linearGradient>
        <linearGradient id="goldband" x1="0" y1="0" x2="1" y2="0">
          <stop offset="0" stop-color="#f2bd2a"/>
          <stop offset="0.5" stop-color="#fbe39a"/>
          <stop offset="1" stop-color="#f2bd2a"/>
        </linearGradient>
        <linearGradient id="skyband" x1="0" y1="0" x2="1" y2="0">
          <stop offset="0" stop-color="#6cb6e4"/>
          <stop offset="0.6" stop-color="#1f74b9"/>
          <stop offset="1" stop-color="#1f74b9"/>
        </linearGradient>
        <linearGradient id="shade" x1="0" y1="0" x2="0" y2="1">
          <stop offset="0" stop-color="#ffffff" stop-opacity="0"/>
          <stop offset="1" stop-color="#c9cbd8" stop-opacity="0.8"/>
        </linearGradient>
        <linearGradient id="texturewash" x1="0" y1="0" x2="1" y2="0">
          <stop offset="0" stop-color="#ffffff"/>
          <stop offset="0.3" stop-color="#f1f2f6"/>
          <stop offset="0.7" stop-color="#f4f4f8"/>
          <stop offset="1" stop-color="#ffffff"/>
        </linearGradient>
      </defs>

      <rect class="card__illustration card__illustration--tangle" x="150" y="130" width="330" height="250" rx="20"
            fill="url(#tanglewash)" role="img"
            aria-label="Illustration: a tangled blue line dotted with gold beads"/>
      <rect class="card__illustration card__illustration--bars" x="610" y="40" width="380" height="300" rx="14"
            fill="url(#barswash)" role="img"
            aria-label="Illustration: the line unravelling into neat, ordered bars with gold beads"/>

      <path class="swoosh__shade" d="M0,430 Q520,560 1200,320 L1200,360 Q520,600 0,470 Z" fill="url(#shade)"/>
      <path class="swoosh__sky" d="M0,460 Q520,600 1200,340 L1200,420 Q560,660 0,520 Z" fill="url(#skyband)"/>
      <path class="swoosh__gold" d="M0,510 Q560,655 1200,410 L1200,440 Q580,680 0,545 Z" fill="url(#goldband)"/>
      <path class="band--navy" d="M0,540 Q580,675 1200,435 L1200,690 L0,690 Z" fill="var(--navy)"/>
      <rect class="strip" x="0" y="690" width="1200" height="150" fill="var(--paper)"/>
      <rect class="strip__texture" x="0" y="692" width="1200" height="148" fill="url(#texturewash)"
            role="img" aria-label="Faint grey scribble texture behind the contact details"/>
      <line x1="0" y1="690" x2="1200" y2="690" stroke="var(--strip-line)" stroke-width="2"/>
    </svg>

    <div class="titles">
      <span>Life Coach</span><span class="titles__dot"></span>
      <span>Professional Adventurer</span><span class="titles__dot"></span>
      <span>Entrepreneur</span>
    </div>

    <div class="contact">
      <span class="contact__name">Dan Pellow</span>
      <span class="contact__web">itsdanp.com.au</span>
      <span class="contact__phone">0468215903</span>
    </div>
  </main>
</body>
</html>
```